skincare creams for tired moms

I need a package and a logo design for a skincare company based in California called Lumen Petal. I make day and night cream, under eye cream, and body lotion. The first product I plan to launch is an under eye cream. It does not have to be in these colors but I do teals, greens, black, and cobalt blue.

The package is going to either be in a box or a bag. Either way I go it will be like a gift box or bag. The design should make the person feel like they are getting something special and luxurious just for them.

I have small kids and it is really difficult to find a chunk of time to myself to update or review.

Target Market(s)

mainly first time moms. I am making an under eye cream that does not use retinol but is still powerful enough to get rid of bags and dark circles.

Industry/Entity Type

Cosmetics

Logo Text

The package and logo should incorporate the name Lumen Petal.

Font styles to use
Decorative
Script

Colors

Designer to choose colors to be used in the design.

Requirements
Nice to have
• maybe focus more on Petal instead of Lumen. Also incorporate plants or flowers
Should not have
• not a huge fan of pink

```html
<!DOCTYPE html>
<html lang="en">
<head>
<meta charset="utf-8">
<title>Lumen Petal – Under Eye Cream Carton</title>
<link href="https://fonts.googleapis.com/css2?family=Montserrat:wght@400;500;600&display=swap" rel="stylesheet">
<style>
  :root {
    --stage: #e8e8e8;
    --paper: #ffffff;
    --teal: #3fb8b2;
    --teal-soft: #8fd6d1;
    --ink: #4a4a4a;
    --ink-soft: #7a7a7a;
    --fold: #d9d9d9;
  }
  * { box-sizing: border-box; margin: 0; padding: 0; }
  html, body { width: 1200px; height: 1200px; overflow: hidden; }
  body {
    background: var(--stage);
    font-family: "Montserrat", sans-serif;
    color: var(--ink);
  }
  .carton {
    position: absolute;
    left: 100px; top: 160px;
    width: 1000px; height: 880px;
    display: flex;
    box-shadow: 0 20px 40px rgba(0,0,0,0.08);
  }
  .panel {
    position: relative;
    height: 100%;
    background: linear-gradient(180deg, #fbfbfb 0%, var(--paper) 60%);
    border-right: 1px solid var(--fold);
    overflow: hidden;
  }
  .panel:last-child { border-right: none; }
  .panel--side { width: 200px; }
  .panel--main { width: 300px; }
  .band {
    position: absolute;
    left: 0; right: 0; bottom: 0;
    height: 200px;
    background: var(--teal);
  }
  .brand {
    position: absolute;
    left: 0; right: 0;
    display: flex; flex-direction: column; align-items: center;
  }
  .brand__mark {
    width: 70px; height: 70px;
    border: 5px solid var(--teal);
    border-radius: 50%;
    margin-bottom: 16px;
  }
  .brand__name {
    font-weight: 600;
    font-size: 26px;
    letter-spacing: -0.5px;
    color: var(--ink);
  }
  .brand__tag {
    margin-top: 4px;
    padding-top: 3px;
    border-top: 1px solid var(--teal);
    font-size: 9px;
    letter-spacing: 3px;
    color: var(--teal);
  }
  .brand--small .brand__name { font-size: 15px; }
  .brand--small .brand__mark { width: 40px; height: 40px; border-width: 3px; margin-bottom: 10px; }
  .product-title {
    position: absolute;
    left: 0; right: 0; top: 400px;
    text-align: center;
    font-weight: 500;
    font-size: 44px;
    line-height: 1.2;
    letter-spacing: 2px;
    color: var(--ink);
  }
  .leaf-art {
    position: absolute;
    left: 75px; top: 620px;
    width: 150px; height: 150px;
    border-radius: 50%;
    background: radial-gradient(circle, var(--teal-soft) 0%, #5cc4be 70%, var(--teal) 100%);
  }
  .volume {
    position: absolute;
    left: 0; right: 0; bottom: 26px;
    text-align: center;
    font-size: 13px;
    letter-spacing: 1px;
    color: var(--teal-soft);
  }
  .band-copy {
    position: absolute;
    left: 20px; right: 20px; bottom: 40px;
    font-size: 10.5px;
    line-height: 1.6;
    color: #e4f6f5;
  }
  .band-copy strong { display: block; margin-top: 8px; font-weight: 600; }
  .back-copy {
    position: absolute;
    left: 30px; right: 30px; top: 560px;
    font-size: 13px;
    line-height: 1.55;
    text-align: center;
    color: var(--ink);
  }
  .back-icons {
    position: absolute;
    left: 0; right: 0; top: 640px;
    display: flex; justify-content: center; gap: 18px;
  }
  .back-icons svg { width: 32px; height: 32px; }
  .code-panel {
    position: absolute;
    left: 50px; right: 50px; bottom: 40px;
    height: 90px;
    background: var(--paper);
  }
</style>
</head>
<body>
  <main class="carton">
    <!-- left side: directions -->
    <section class="panel panel--side">
      <div class="brand brand--small" style="top:90px">
        <div class="brand__mark"></div>
        <div class="brand__name">Lumen Petal</div>
      </div>
      <div class="band">
        <p class="band-copy">Recommended use: Apply Lumen Petal under eye cream on clean and relaxed skin and massage gently.
          <strong>www.lumenpetal.com</strong></p>
      </div>
    </section>

    <!-- front -->
    <section class="panel panel--main">
      <div class="brand" style="top:90px">
        <div class="brand__mark"></div>
        <div class="brand__name">Lumen Petal</div>
        <div class="brand__tag">SKINCARE</div>
      </div>
      <h1 class="product-title">UNDER<br>EYE<br>CREAM</h1>
      <div class="band">
        <p class="volume">30 ML / 1 FL OZ</p>
      </div>
      <div class="leaf-art" role="img" aria-label="Round cluster of leafy branches"></div>
    </section>

    <!-- right side: ingredients -->
    <section class="panel panel--side">
      <div class="brand brand--small" style="top:90px">
        <div class="brand__mark"></div>
        <div class="brand__name">Lumen Petal</div>
      </div>
      <div class="band">
        <p class="band-copy">Ingredients: Aqua, Propanediol, Urea, Glycerin, Sodium Lactate, Sodium Hyaluronate, Zinc Pca, Hydroxyacetophenone, Lactic Acid, 1,2-hexanediol, Caprylyl Glycol</p>
      </div>
    </section>

    <!-- back -->
    <section class="panel panel--main">
      <div class="brand" style="top:90px">
        <div class="brand__mark"></div>
        <div class="brand__name">Lumen Petal</div>
        <div class="brand__tag">SKINCARE</div>
      </div>
      <p class="back-copy">Manufactured and filled with great care in xxxxxxx for: Lumen Petal Street Name, Number, City, State, Country</p>
      <div class="back-icons">
        <svg viewBox="0 0 32 32" aria-label="Period after opening: 6 months"><rect x="4" y="12" width="24" height="16" rx="2" fill="none" stroke="#4a4a4a" stroke-width="2"/><path d="M6 12 L12 4 L26 8" fill="none" stroke="#4a4a4a" stroke-width="2"/></svg>
        <svg viewBox="0 0 32 32" aria-label="Vegan badge"><circle cx="16" cy="16" r="12" fill="none" stroke="#4a4a4a" stroke-width="2"/></svg>
        <svg viewBox="0 0 32 32" aria-label="Cruelty free badge"><circle cx="16" cy="16" r="12" fill="none" stroke="#4a4a4a" stroke-width="2"/></svg>
        <svg viewBox="0 0 32 32" aria-label="Recyclable"><path d="M16 5 L24 18 H8 Z" fill="none" stroke="#4a4a4a" stroke-width="2.5" stroke-linejoin="round"/><path d="M6 24 H26" stroke="#4a4a4a" stroke-width="2.5"/></svg>
      </div>
      <div class="band">
        <div class="code-panel"></div>
      </div>
    </section>
  </main>
</body>
</html>
```